Supplement Company needs final product mockups and label design

We're a Supplement company launching 4 Hydration Supplement flavours. We need someone to re create the EXACT design with what QuillBot has already generated and tweak the design slightly so that spelling is correct and callout icons are designed. We then also need someone to do the back of label design that includes space for the barcode, nutrition table, blurb etc. Bonus if you have experience with PRELK compliance regulations and designing supplement labels.

We want the other 3 flavours (Lime, Mango & Watermelon) to match the design of the strawberry flavour including details like all the callout icons on the left side of the front, the word "electrolytes" in the dark coloured box, the words "hydration powder" just above the callout icons. Please re - design the callout icons to better suit the callout.

I've also attached an image of what the nutrition label should look like.

Please include the Following on the back of the label:
"Directions: Mix 1 Scoop with 400-500ml of water & Mix well before drinking. Do not exceed 2 servings per day.

Why settle when you can VOLTRA?
Your body wasn’t made to run on sugar, chemicals, and artificial junk — and your hydration shouldn’t either. At VOLTRA Nutrition, we’ve created a clean, mineral-rich formula with Morvane Brine and essential electrolytes to fuel you the right way. No toxins, no fillers — just real ingredients that work with your body, not against it.
Hydrate the way nature intended. Live clean. VOLTRA.

AUSTRALIAN OWNED AND MADE

Store in a cool, dry place below 30°C. Reseal after use"

Product Formula & Ingredients:

* Sodium (Sea Salt, Morvane Brine®, Himalayan Pink Salt): 1000 mg
* Potassium (from Potassium Chloride): 200 mg
* Magnesium (from Magnesium Glycinate): 60 mg
* Total Carbohydrates: 0 g
* Sugars: 0 g
* Calories: 1 kcal

Ingredients:
Sea Salt, Citric Acid, Morvane Brine®, Himalayan Pink Salt, Potassium Chloride, Magnesium Glycinate, Natural Flavour (e.g. Mango), Stevia Leaf Extract.

I would like to give designers more time to closely replicate what I have included in the brief and make sure they can create something very beautifully

Industry/Entity Type

Supplements

Font styles to use
Other font styles liked:
• Montserrat

Requirements
Must have
• Back of label design aswell and Australian Nutrition table
Nice to have
• Design as close to the Provided images as possible
Should not have
• Should not be too different to the attached images

```html
<!DOCTYPE html>
<html lang="en">
<head>
<meta charset="utf-8">
<title>VOLTRA Nutrition – Electrolytes Hydration Powder Labels</title>
<link rel="stylesheet" href="https://fonts.googleapis.com/css2?family=Anton&family=Montserrat:wght@400;500;600;700;800;900&family=Oswald:wght@600;700&display=swap">
<style>
  :root{
    --ink:#1b1b1b;
    --white:#ffffff;
    --dark-box:#231f20;
    --straw-bg:#d71f26; --straw-lab:#c91c22; --straw-lab2:#e1342f; --straw-fruit1:#f04a3a; --straw-fruit2:#b5121b;
    --lime-bg:#b7d432; --lime-lab:#8dbb2c; --lime-lab2:#a9cf3a; --lime-fruit1:#9bd43a; --lime-fruit2:#3f8f1f;
    --mango-bg:#f5a01a; --mango-lab:#f08a12; --mango-lab2:#f7ad22; --mango-fruit1:#fbbf2a; --mango-fruit2:#e8641a;
    --melon-bg:#ea3a78; --melon-lab:#dd2764; --melon-lab2:#ef4c86; --melon-fruit1:#e8403e; --melon-fruit2:#2f6b2a;
  }
  *{box-sizing:border-box;margin:0;padding:0}
  html,body{width:749px;height:1200px;overflow:hidden;background:#fff}
  body{font-family:"Montserrat",sans-serif;color:var(--white)}
  .sheet{width:749px;height:1200px;position:relative}
  .band{position:absolute;left:0;width:749px;height:300px;background:var(--bg)}
  .band--straw{top:0;--bg:var(--straw-bg);--lab:var(--straw-lab);--lab2:var(--straw-lab2);--f1:var(--straw-fruit1);--f2:var(--straw-fruit2)}
  .band--lime{top:300px;--bg:var(--lime-bg);--lab:var(--lime-lab);--lab2:var(--lime-lab2);--f1:var(--lime-fruit1);--f2:var(--lime-fruit2)}
  .band--mango{top:600px;--bg:var(--mango-bg);--lab:var(--mango-lab);--lab2:var(--mango-lab2);--f1:var(--mango-fruit1);--f2:var(--mango-fruit2)}
  .band--melon{top:900px;--bg:var(--melon-bg);--lab:var(--melon-lab);--lab2:var(--melon-lab2);--f1:var(--melon-fruit1);--f2:var(--melon-fruit2)}

  .label{position:absolute;left:55px;top:64px;width:470px;height:189px;
    background:linear-gradient(120deg,var(--lab) 0%,var(--lab2) 50%,var(--lab) 100%);
    box-shadow:0 2px 6px rgba(0,0,0,.18)}
  .front{position:absolute;left:528px;top:64px;width:160px;height:200px;border-radius:6px;
    background:linear-gradient(120deg,var(--lab) 0%,var(--lab2) 55%,var(--lab) 100%);
    box-shadow:0 2px 6px rgba(0,0,0,.18)}

  .blurb{position:absolute;left:12px;top:27px;width:124px;font-size:5.1px;line-height:6.75px;text-align:justify;font-weight:500}
  .blurb p{margin-bottom:3px}
  .blurb b{font-weight:800;font-style:italic;color:var(--ink)}
  .blurb .lead{font-weight:700;color:var(--ink)}
  .blurb .store{text-align:center}

  .brand{position:absolute;left:0;width:100%;text-align:center}
  .brand-name{font-family:"Montserrat",sans-serif;font-weight:900;font-size:17px;letter-spacing:.5px;line-height:16px}
  .brand-sub{font-weight:600;font-size:5.5px;letter-spacing:1.6px;line-height:6px}
  .flavour{font-family:"Anton",sans-serif;font-size:25px;line-height:25px;letter-spacing:.3px;margin-top:1px}
  .elec{display:inline-block;background:var(--dark-box);border-radius:4px;padding:1px 6px 0;font-weight:800;font-size:13.5px;line-height:16px;letter-spacing:.4px;margin-top:1px}
  .powder{font-weight:700;font-size:8.5px;letter-spacing:.3px;margin-top:3px}

  .col{position:absolute;left:142px;top:15px;width:184px}
  .claims{position:absolute;left:33px;top:88px;list-style:none}
  .claims li{display:flex;align-items:center;gap:3px;height:17px;font-size:5px;line-height:5.3px;font-weight:600}
  .claims svg{width:12px;height:12px;flex:none}
  .fruit{position:absolute;left:75px;top:82px;width:82px;height:76px;border-radius:50%;
    background:radial-gradient(circle at 40% 38%,var(--f1) 0%,var(--f2) 85%)}
  .netwt{position:absolute;left:0;width:100%;top:162px;text-align:center;font-family:"Oswald",sans-serif;font-weight:700;font-size:9.5px;letter-spacing:.3px}

  .nip{position:absolute;left:333px;top:28px;width:96px;height:101px;background:var(--white);color:var(--ink);border:1px solid var(--ink);padding:3px 4px;font-size:3.6px;line-height:4.6px}
  .nip h3{font-size:6px;font-weight:700;text-align:center;line-height:8px}
  .nip table{width:100%;border-collapse:collapse;margin-top:2px}
  .nip th{font-weight:500;text-align:center;border-bottom:.6px solid var(--ink);border-top:.6px solid var(--ink)}
  .nip td{text-align:center;padding:.6px 0}
  .nip td:first-child,.nip th:first-child{text-align:left}
  .badge{position:absolute;left:434px;top:28px;width:10px;height:10px;background:var(--white);border-radius:2px}
  .origin{position:absolute;left:445px;top:28px;font-size:3.4px;font-weight:700;writing-mode:vertical-rl;transform:rotate(180deg);line-height:4px}
  .ingredients{position:absolute;left:333px;top:135px;width:126px;font-size:5.3px;line-height:7.2px;text-align:justify;font-weight:500}
  .ingredients b{color:var(--ink);font-weight:700}

  .front .col{left:0;top:15px;width:100%}
  .front .flavour{font-size:23px;line-height:24px}
  .front .elec{font-size:12.5px}
  .front .powder{font-size:8px}
  .front .claims{left:28px;top:86px}
  .front .fruit{left:72px;top:84px;width:62px;height:66px}
  .front .netwt{top:164px}
</style>
</head>
<body>
<main class="sheet">

<!-- reusable claim icons -->
<svg width="0" height="0" style="position:absolute">
  <defs>
    <g id="ico-keto"><circle cx="6" cy="6" r="5.5" fill="#1b1b1b"/><path d="M6 2.8c-1.6 1.9-2.3 3.3-2.3 4.4a2.3 2.3 0 0 0 4.6 0C8.3 6.1 7.6 4.7 6 2.8z" fill="none" stroke="#fff" stroke-width=".8"/></g>
    <g id="ico-sugar"><circle cx="6" cy="6" r="5.5" fill="#1b1b1b"/><rect x="4" y="4" width="4" height="4" fill="none" stroke="#fff" stroke-width=".8"/><path d="M3 9 9 3" stroke="#fff" stroke-width=".8"/></g>
    <g id="ico-paleo"><circle cx="6" cy="6" r="5.5" fill="#1b1b1b"/><path d="M3.5 8.5C4 5 6 3.5 8.6 3.4 8.5 6 7 8 3.5 8.5zM3.5 8.5 7 5" fill="none" stroke="#fff" stroke-width=".8"/></g>
    <g id="ico-gluten"><circle cx="6" cy="6" r="5.5" fill="#1b1b1b"/><path d="M6 2.6v7M6 4.2 4.6 3.3M6 4.2 7.4 3.3M6 6 4.6 5.1M6 6 7.4 5.1M6 7.8 4.6 6.9M6 7.8 7.4 6.9" stroke="#fff" stroke-width=".8" fill="none"/></g>
  </defs>
</svg>

<!-- STRAWBERRY -->
<section class="band band--straw">
  <article class="label">
    <div class="blurb">
      <p>Why settle when you can <b>VOLTRA?</b> Your body wasn’t made to run on sugar, chemicals, and artificial junk, and your hydration shouldn’t either. At <b>VOLTRA</b> Nutrition, we’ve created a clean, mineral-rich formula with Morvane Brine and essential electrolytes to fuel you the right way. No toxins, no fillers, just real ingredients that work with your body, not against it. Hydrate the way nature intended. Live clean. <b>VOLTRA.</b></p>
      <p><span class="lead">Directions:</span> Mix 1 Scoop with 400-500ml of water &amp; Mix well before drinking. Do not exceed 2 servings per day.</p>
      <p><span class="lead">Manufactured by:</span> <b>VOLTRA</b> Nutrition, 48 Tidewell Rd, Sydney, Australia. Contact: info@voltra.com | +61 400 555 019 Made in Australia | Batch No: 12345 | Best Before: 28/04/2026</p>
      <p class="store">Store in a cool, dry place below 30°C.<br>Reseal after use</p>
    </div>
    <div class="col">
      <div class="brand"><div class="brand-name">VOLTRA</div><div class="brand-sub">NUTRITION</div><div class="flavour">STRAWBERRY</div><div class="elec">ELECTROLYTES</div><div class="powder">HYDRATION POWDER</div></div>
      <ul class="claims">
        <li><svg viewBox="0 0 12 12"><use href="#ico-keto"/></svg>KETO<br>FRIENDLY</li>
        <li><svg viewBox="0 0 12 12"><use href="#ico-sugar"/></svg>SUGAR<br>FREE</li>
        <li><svg viewBox="0 0 12 12"><use href="#ico-paleo"/></svg>PALEO<br>FRIENDLY</li>
        <li><svg viewBox="0 0 12 12"><use href="#ico-gluten"/></svg>GLUTEN<br>FREE</li>
      </ul>
      <div class="fruit" role="img" aria-label="Illustration of a ripe strawberry"></div>
    </div>
    <div class="nip">
      <h3>Nutrition Information</h3>
      <div>Servings per package: 1.00<br>Serving size: 350.00 g</div>
      <table>
        <tr><th></th><th>Average per Serving</th><th>Average per 100 g</th></tr>
        <tr><td>Energy</td><td>4 kJ</td><td>40 kJ</td></tr>
        <tr><td>Protein</td><td>0.0 g</td><td>0.0 g</td></tr>
        <tr><td>Fat, total<br>- saturated</td><td>0.0 g</td><td>0.0 g</td></tr>
        <tr><td>Carbohydrate<br>- sugars</td><td>0.0 g</td><td>0.0 g</td></tr>
        <tr><td>Sodium</td><td>1000 mg</td><td>10000 mg</td></tr>
        <tr><td>Potassium</td><td>200 mg</td><td>2000 mg</td></tr>
        <tr><td>Magnesium</td><td>60 mg</td><td>600 mg</td></tr>
      </table>
    </div>
    <div class="badge"></div><div class="origin">AUSTRALIAN OWNED<br>AND MADE</div>
    <p class="ingredients"><b>Ingredients:</b> Sea Salt, Citric Acid, Morvane Brine®, Himalayan Pink Salt, Potassium Chloride, Magnesium Glycinate, Natural Flavour (e.g. Mango), Stevia Leaf Extract.</p>
  </article>
  <article class="front">
    <div class="col">
      <div class="brand"><div class="brand-name">VOLTRA</div><div class="brand-sub">NUTRITION</div><div class="flavour">STRAWBERRY</div><div class="elec">ELECTROLYTES</div><div class="powder">HYDRATION POWDER</div></div>
      <ul class="claims">
        <li><svg viewBox="0 0 12 12"><use href="#ico-keto"/></svg>KETO<br>FRIENDLY</li>
        <li><svg viewBox="0 0 12 12"><use href="#ico-sugar"/></svg>SUGAR<br>FREE</li>
        <li><svg viewBox="0 0 12 12"><use href="#ico-paleo"/></svg>PALEO<br>FRIENDLY</li>
        <li><svg viewBox="0 0 12 12"><use href="#ico-gluten"/></svg>GLUTEN<br>FREE</li>
      </ul>
      <div class="fruit" role="img" aria-label="Illustration of a ripe strawberry"></div>
      <div class="netwt">NET WT. 180g</div>
    </div>
  </article>
</section>

<!-- LIME -->
<section class="band band--lime">
  <article class="label">
    <div class="blurb">
      <p>Why settle when you can <b>VOLTRA?</b> Your body wasn’t made to run on sugar, chemicals, and artificial junk, and your hydration shouldn’t either. At <b>VOLTRA</b> Nutrition, we’ve created a clean, mineral-rich formula with Morvane Brine and essential electrolytes to fuel you the right way. No toxins, no fillers, just real ingredients that work with your body, not against it. Hydrate the way nature intended. Live clean. <b>VOLTRA.</b></p>
      <p><span class="lead">Directions:</span> Mix 1 Scoop with 400-500ml of water &amp; Mix well before drinking. Do not exceed 2 servings per day.</p>
      <p><span class="lead">Manufactured by:</span> <b>VOLTRA</b> Nutrition, 48 Tidewell Rd, Sydney, Australia. Contact: info@voltra.com | +61 400 555 019 Made in Australia | Batch No: 12345 | Best Before: 28/04/2026</p>
      <p class="store">Store in a cool, dry place below 30°C.<br>Reseal after use</p>
    </div>
    <div class="col">
      <div class="brand"><div class="brand-name">VOLTRA</div><div class="brand-sub">NUTRITION</div><div class="flavour">LIME</div><div class="elec">ELECTROLYTES</div><div class="powder">HYDRATION POWDER</div></div>
      <ul class="claims">
        <li><svg viewBox="0 0 12 12"><use href="#ico-keto"/></svg>KETO<br>FRIENDLY</li>
        <li><svg viewBox="0 0 12 12"><use href="#ico-sugar"/></svg>SUGAR<br>FREE</li>
        <li><svg viewBox="0 0 12 12"><use href="#ico-paleo"/></svg>PALEO<br>FRIENDLY</li>
        <li><svg viewBox="0 0 12 12"><use href="#ico-gluten"/></svg>GLUTEN<br>FREE</li>
      </ul>
      <div class="fruit" role="img" aria-label="Illustration of a whole lime and a lime slice"></div>
      <div class="netwt">NET WT. 180g</div>
    </div>
    <div class="nip">
      <h3>Nutrition Information</h3>
      <div>Servings per package: 1.00<br>Serving size: 350.00 g</div>
      <table>
        <tr><th></th><th>Average per Serving</th><th>Average per 100 g</th></tr>
        <tr><td>Energy</td><td>4 kJ</td><td>40 kJ</td></tr>
        <tr><td>Protein</td><td>0.0 g</td><td>0.0 g</td></tr>
        <tr><td>Fat, total<br>- saturated</td><td>0.0 g</td><td>0.0 g</td></tr>
        <tr><td>Carbohydrate<br>- sugars</td><td>0.0 g</td><td>0.0 g</td></tr>
        <tr><td>Sodium</td><td>1000 mg</td><td>10000 mg</td></tr>
        <tr><td>Potassium</td><td>200 mg</td><td>2000 mg</td></tr>
        <tr><td>Magnesium</td><td>60 mg</td><td>600 mg</td></tr>
      </table>
    </div>
    <div class="badge"></div><div class="origin">AUSTRALIAN OWNED<br>AND MADE</div>
    <p class="ingredients"><b>Ingredients:</b> Sea Salt, Citric Acid, Morvane Brine®, Himalayan Pink Salt, Potassium Chloride, Magnesium Glycinate, Natural Flavour (e.g. Mango), Stevia Leaf Extract.</p>
  </article>
  <article class="front">
    <div class="col">
      <div class="brand"><div class="brand-name">VOLTRA</div><div class="brand-sub">NUTRITION</div><div class="flavour">LIME</div><div class="elec">ELECTROLYTES</div><div class="powder">HYDRATION POWDER</div></div>
      <ul class="claims">
        <li><svg viewBox="0 0 12 12"><use href="#ico-keto"/></svg>KETO<br>FRIENDLY</li>
        <li><svg viewBox="0 0 12 12"><use href="#ico-sugar"/></svg>SUGAR<br>FREE</li>
        <li><svg viewBox="0 0 12 12"><use href="#ico-paleo"/></svg>PALEO<br>FRIENDLY</li>
        <li><svg viewBox="0 0 12 12"><use href="#ico-gluten"/></svg>GLUTEN<br>FREE</li>
      </ul>
      <div class="fruit" role="img" aria-label="Illustration of a whole lime and a lime slice"></div>
      <div class="netwt">NET WT. 180g</div>
    </div>
  </article>
</section>

<!-- MANGO -->
<section class="band band--mango">
  <article class="label">
    <div class="blurb">
      <p>Why settle when you can <b>VOLTRA?</b> Your body wasn’t made to run on sugar, chemicals, and artificial junk, and your hydration shouldn’t either. At <b>VOLTRA</b> Nutrition, we’ve created a clean, mineral-rich formula with Morvane Brine and essential electrolytes to fuel you the right way. No toxins, no fillers, just real ingredients that work with your body, not against it. Hydrate the way nature intended. Live clean. <b>VOLTRA.</b></p>
      <p><span class="lead">Directions:</span> Mix 1 Scoop with 400-500ml of water &amp; Mix well before drinking. Do not exceed 2 servings per day.</p>
      <p><span class="lead">Manufactured by:</span> <b>VOLTRA</b> Nutrition, 48 Tidewell Rd, Sydney, Australia. Contact: info@voltra.com | +61 400 555 019 Made in Australia | Batch No: 12345 | Best Before: 28/04/2026</p>
      <p class="store">Store in a cool, dry place below 30°C.<br>Reseal after use</p>
    </div>
    <div class="col">
      <div class="brand"><div class="brand-name">VOLTRA</div><div class="brand-sub">NUTRITION</div><div class="flavour">MANGO</div><div class="elec">ELECTROLYTES</div><div class="powder">HYDRATION POWDER</div></div>
      <ul class="claims">
        <li><svg viewBox="0 0 12 12"><use href="#ico-keto"/></svg>KETO<br>FRIENDLY</li>
        <li><svg viewBox="0 0 12 12"><use href="#ico-sugar"/></svg>SUGAR<br>FREE</li>
        <li><svg viewBox="0 0 12 12"><use href="#ico-paleo"/></svg>PALEO<br>FRIENDLY</li>
        <li><svg viewBox="0 0 12 12"><use href="#ico-gluten"/></svg>GLUTEN<br>FREE</li>
      </ul>
      <div class="fruit" role="img" aria-label="Illustration of a ripe mango with leaf"></div>
      <div class="netwt">NET WT. 180g</div>
    </div>
    <div class="nip">
      <h3>Nutrition Information</h3>
      <div>Servings per package: 1.00<br>Serving size: 350.00 g</div>
      <table>
        <tr><th></th><th>Average per Serving</th><th>Average per 100 g</th></tr>
        <tr><td>Energy</td><td>4 kJ</td><td>40 kJ</td></tr>
        <tr><td>Protein</td><td>0.0 g</td><td>0.0 g</td></tr>
        <tr><td>Fat, total<br>- saturated</td><td>0.0 g</td><td>0.0 g</td></tr>
        <tr><td>Carbohydrate<br>- sugars</td><td>0.0 g</td><td>0.0 g</td></tr>
        <tr><td>Sodium</td><td>1000 mg</td><td>10000 mg</td></tr>
        <tr><td>Potassium</td><td>200 mg</td><td>2000 mg</td></tr>
        <tr><td>Magnesium</td><td>60 mg</td><td>600 mg</td></tr>
      </table>
    </div>
    <div class="badge"></div><div class="origin">AUSTRALIAN OWNED<br>AND MADE</div>
    <p class="ingredients"><b>Ingredients:</b> Sea Salt, Citric Acid, Morvane Brine®, Himalayan Pink Salt, Potassium Chloride, Magnesium Glycinate, Natural Flavour (e.g. Mango), Stevia Leaf Extract.</p>
  </article>
  <article class="front">
    <div class="col">
      <div class="brand"><div class="brand-name">VOLTRA</div><div class="brand-sub">NUTRITION</div><div class="flavour">MANGO</div><div class="elec">ELECTROLYTES</div><div class="powder">HYDRATION POWDER</div></div>
      <ul class="claims">
        <li><svg viewBox="0 0 12 12"><use href="#ico-keto"/></svg>KETO<br>FRIENDLY</li>
        <li><svg viewBox="0 0 12 12"><use href="#ico-sugar"/></svg>SUGAR<br>FREE</li>
        <li><svg viewBox="0 0 12 12"><use href="#ico-paleo"/></svg>PALEO<br>FRIENDLY</li>
        <li><svg viewBox="0 0 12 12"><use href="#ico-gluten"/></svg>GLUTEN<br>FREE</li>
      </ul>
      <div class="fruit" role="img" aria-label="Illustration of a ripe mango with leaf"></div>
      <div class="netwt">NET WT. 180g</div>
    </div>
  </article>
</section>

<!-- WATERMELON -->
<section class="band band--melon">
  <article class="label">
    <div class="blurb">
      <p>Why settle when you can <b>VOLTRA?</b> Your body wasn’t made to run on sugar, chemicals, and artificial junk, and your hydration shouldn’t either. At <b>VOLTRA</b> Nutrition, we’ve created a clean, mineral-rich formula with Morvane Brine and essential electrolytes to fuel you the right way. No toxins, no fillers, just real ingredients that work with your body, not against it. Hydrate the way nature intended. Live clean. <b>VOLTRA.</b></p>
      <p><span class="lead">Directions:</span> Mix 1 Scoop with 400-500ml of water &amp; Mix well before drinking. Do not exceed 2 servings per day.</p>
      <p><span class="lead">Manufactured by:</span> <b>VOLTRA</b> Nutrition, 48 Tidewell Rd, Sydney, Australia. Contact: info@voltra.com | +61 400 555 019 Made in Australia | Batch No: 12345 | Best Before: 28/04/2026</p>
      <p class="store">Store in a cool, dry place below 30°C.<br>Reseal after use</p>
    </div>
    <div class="col">
      <div class="brand"><div class="brand-name">VOLTRA</div><div class="brand-sub">NUTRITION</div><div class="flavour">WATERMELON</div><div class="elec">ELECTROLYTES</div><div class="powder">HYDRATION POWDER</div></div>
      <ul class="claims">
        <li><svg viewBox="0 0 12 12"><use href="#ico-keto"/></svg>KETO<br>FRIENDLY</li>
        <li><svg viewBox="0 0 12 12"><use href="#ico-sugar"/></svg>SUGAR<br>FREE</li>
        <li><svg viewBox="0 0 12 12"><use href="#ico-paleo"/></svg>PALEO<br>FRIENDLY</li>
        <li><svg viewBox="0 0 12 12"><use href="#ico-gluten"/></svg>GLUTEN<br>FREE</li>
      </ul>
      <div class="fruit" role="img" aria-label="Illustration of a watermelon and a watermelon slice"></div>
      <div class="netwt">NET WT. 180g</div>
    </div>
    <div class="nip">
      <h3>Nutrition Information</h3>
      <div>Servings per package: 1.00<br>Serving size: 350.00 g</div>
      <table>
        <tr><th></th><th>Average per Serving</th><th>Average per 100 g</th></tr>
        <tr><td>Energy</td><td>4 kJ</td><td>40 kJ</td></tr>
        <tr><td>Protein</td><td>0.0 g</td><td>0.0 g</td></tr>
        <tr><td>Fat, total<br>- saturated</td><td>0.0 g</td><td>0.0 g</td></tr>
        <tr><td>Carbohydrate<br>- sugars</td><td>0.0 g</td><td>0.0 g</td></tr>
        <tr><td>Sodium</td><td>1000 mg</td><td>10000 mg</td></tr>
        <tr><td>Potassium</td><td>200 mg</td><td>2000 mg</td></tr>
        <tr><td>Magnesium</td><td>60 mg</td><td>600 mg</td></tr>
      </table>
    </div>
    <div class="badge"></div><div class="origin">AUSTRALIAN OWNED<br>AND MADE</div>
    <p class="ingredients"><b>Ingredients:</b> Sea Salt, Citric Acid, Morvane Brine®, Himalayan Pink Salt, Potassium Chloride, Magnesium Glycinate, Natural Flavour (e.g. Mango), Stevia Leaf Extract.</p>
  </article>
  <article class="front">
    <div class="col">
      <div class="brand"><div class="brand-name">VOLTRA</div><div class="brand-sub">NUTRITION</div><div class="flavour">WATERMELON</div><div class="elec">ELECTROLYTES</div><div class="powder">HYDRATION POWDER</div></div>
      <ul class="claims">
        <li><svg viewBox="0 0 12 12"><use href="#ico-keto"/></svg>KETO<br>FRIENDLY</li>
        <li><svg viewBox="0 0 12 12"><use href="#ico-sugar"/></svg>SUGAR<br>FREE</li>
        <li><svg viewBox="0 0 12 12"><use href="#ico-paleo"/></svg>PALEO<br>FRIENDLY</li>
        <li><svg viewBox="0 0 12 12"><use href="#ico-gluten"/></svg>GLUTEN<br>FREE</li>
      </ul>
      <div class="fruit" role="img" aria-label="Illustration of a watermelon and a watermelon slice"></div>
      <div class="netwt">NET WT. 180g</div>
    </div>
  </article>
</section>

</main>
</body>
</html>
```